Real Estate agent needs flyer/folder to contain bio and overview of services

I'm including files of the layout of the small folder. The folder is 6 1/2 across and 9 1/2 inches long. It will have a front & back cover and then writing on the 2 inside pages.

I am sending a few files to incorporate into the flyer, 1 new logo to use and 2 files which are coloring ideas.

```html
<!DOCTYPE html>
<html lang="en">
<head>
<meta charset="utf-8">
<title>Folder Back Cover – Dana Whitfield</title>
<link href="https://fonts.googleapis.com/css2?family=Arimo:ital,wght@0,400;0,700;1,400&display=swap" rel="stylesheet">
<style>
  :root {
    --page-bg: #e9e9ea;
    --card-white: #ffffff;
    --text-dark: #1c1c1c;
    --blue-light: #3f7fd0;
    --blue-mid: #2c62b6;
    --blue-navy: #1f3f98;
    --brand-red: #d7262e;
    --photo-top: #d8c7a2;
    --photo-bottom: #2b2b30;
  }
  * { box-sizing: border-box; margin: 0; padding: 0; }
  html, body {
    width: 900px; height: 1200px; overflow: hidden;
    background: var(--page-bg);
    font-family: "Arimo", Arial, sans-serif;
  }
  .folder-back {
    position: absolute; left: 70px; top: 45px;
    width: 760px; height: 1110px;
    background: var(--card-white);
    box-shadow: 0 4px 18px rgba(0,0,0,0.15);
    overflow: hidden;
  }
  .accent-bands { position: absolute; left: 0; top: 0; width: 760px; height: 1110px; }
  .agent-photo {
    position: absolute; left: 30px; top: 740px;
    width: 230px; height: 240px;
    background: linear-gradient(180deg, var(--photo-top) 0%, #c9a98a 45%, var(--photo-bottom) 100%);
  }
  .agent-message {
    position: absolute; left: 285px; top: 775px; width: 430px;
    font-size: 15.5px; line-height: 1.3; color: var(--text-dark);
  }
  .agent-contact {
    position: absolute; left: 285px; top: 865px;
    font-size: 16px; font-weight: 700; line-height: 1.25; color: var(--text-dark);
    list-style: none;
  }
  .brand-mark {
    position: absolute; left: 470px; top: 935px;
    display: flex; align-items: center; gap: 10px;
  }
  .brand-dot {
    width: 26px; height: 26px; border-radius: 50%;
    background: var(--brand-red);
  }
  .brand-name {
    font-size: 24px; font-weight: 700; color: var(--blue-navy);
  }
  .trade-badges {
    position: absolute; right: 40px; bottom: 28px;
    display: flex; gap: 14px;
  }
  .trade-badge {
    width: 26px; height: 26px; background: var(--card-white);
  }
</style>
</head>
<body>
  <section class="folder-back">
    <svg class="accent-bands" viewBox="0 0 760 1110" aria-hidden="true">
      <polygon points="0,835 0,1110 470,1110" fill="var(--blue-light)"/>
      <polygon points="0,960 0,1110 470,1110" fill="var(--blue-mid)"/>
      <polygon points="300,1040 760,1000 760,1110 300,1110" fill="var(--blue-navy)"/>
    </svg>

    <div class="agent-photo" role="img" aria-label="Portrait photo of the agent, Dana Whitfield"></div>

    <p class="agent-message">Along with being your Realtor, I'm a lifelong resource for all things home-related &amp; beyond…If you need a great referral for anything at all, call me!&nbsp; I can't wait to work with you!</p>

    <ul class="agent-contact">
      <li>Dana Whitfield</li>
      <li>555 014 2278</li>
      <li>Dana@danawhomes.com</li>
      <li>www.danawhomes.com</li>
    </ul>

    <div class="brand-mark">
      <span class="brand-dot"></span>
      <span class="brand-name">Summit Realty</span>
    </div>

    <div class="trade-badges">
      <span class="trade-badge"></span>
      <span class="trade-badge"></span>
    </div>
  </section>
</body>
</html>
```